Business card, Letterhead and envelope design
Create a business card, letterhead and envelope design for Velmira Solutions
Professional
name
title
address
email@velmira-example.com
www.velmirasolutions-example.com
logo and font
Trifold brochure design we have for inspiration of design. This is for reference only.

```html
<!DOCTYPE html>
<html lang="en">
<head>
<meta charset="utf-8">
<title>Velmira Solutions — Business Card</title>
<link rel="stylesheet" href="https://fonts.googleapis.com/css2?family=Questrial&display=swap">
<style>
  :root {
    --page-bg: #e6e9ec;
    --blue-deep: #0a8fd6;
    --blue-mid: #2aa9e8;
    --blue-light: #7fd0f6;
    --blue-pale: #cfeefd;
    --ink: #1d2630;
    --white: #ffffff;
    --mark: #1e2a35;
  }
  * { box-sizing: border-box; margin: 0; padding: 0; }
  html, body {
    width: 1200px; height: 901px; overflow: hidden;
    background: var(--page-bg);
    font-family: "Questrial", "Century Gothic", sans-serif;
  }
  .canvas { position: relative; width: 1200px; height: 901px; }

  .card {
    position: absolute; overflow: hidden;
    box-shadow: 0 6px 18px rgba(0,0,0,.25);
  }
  .card-front { left: 61px; top: 80px; width: 616px; height: 353px; background: var(--white); }
  .card-back {
    left: 528px; top: 487px; width: 609px; height: 348px;
    background: radial-gradient(ellipse at 45% 40%, var(--blue-light) 0%, var(--blue-mid) 45%, var(--blue-deep) 100%);
  }

  .card-shapes { position: absolute; inset: 0; }

  .hero-photo {
    position: absolute; left: 250px; top: 0; width: 366px; height: 250px;
    background: radial-gradient(ellipse at 45% 35%, #bfe6fb 0%, #e6f6fe 45%, rgba(255,255,255,0) 75%);
  }

  .holder-name { position: absolute; left: 49px; top: 30px; font-size: 28px; color: var(--white); }
  .holder-title { position: absolute; left: 49px; top: 64px; font-size: 14px; color: var(--white); }

  .contact { position: absolute; left: 49px; color: var(--ink); font-size: 15px; line-height: 1; }
  .contact-street { top: 124px; }
  .contact-city { top: 146px; }
  .contact-phone { top: 182px; }
  .contact-email { top: 204px; }
  .contact-web { top: 226px; }

  .brand { position: absolute; color: var(--white); text-align: center; line-height: 1.05; }
  .brand-square { position: absolute; background: var(--mark); }

  .card-front .brand-square { left: 456px; top: 216px; width: 60px; height: 60px; }
  .card-front .brand { left: 300px; top: 284px; width: 150px; }
  .card-front .brand-name { font-size: 25px; }
  .card-front .brand-sub { font-size: 17px; }

  .card-back .brand-square { left: 262px; top: 104px; width: 84px; height: 84px; }
  .card-back .brand { left: 0; top: 222px; width: 609px; }
  .card-back .brand-name { font-size: 36px; }
  .card-back .brand-sub { font-size: 24px; margin-top: 6px; }
</style>
</head>
<body>
<main class="canvas">

  <section class="card card-front" aria-label="Business card front">
    <div class="hero-photo" role="img" aria-label="Photo of a network cable with a stream of binary digits in pale blue"></div>
    <svg class="card-shapes" width="616" height="353" viewBox="0 0 616 353" aria-hidden="true">
      <defs>
        <linearGradient id="top-swoosh" x1="0" y1="0" x2="1" y2="1">
          <stop offset="0" stop-color="#0a8fd6"/>
          <stop offset="1" stop-color="#47bdf1"/>
        </linearGradient>
        <linearGradient id="bottom-band" x1="0" y1="0" x2="1" y2="0">
          <stop offset="0" stop-color="#1aa1e4"/>
          <stop offset="1" stop-color="#0a8fd6"/>
        </linearGradient>
      </defs>
      <path d="M0,0 H430 C330,40 230,80 110,90 C70,93 30,95 0,100 Z" fill="url(#top-swoosh)"/>
      <path d="M0,108 C60,98 160,98 250,80 C330,64 400,30 450,0" fill="none" stroke="#2aa9e8" stroke-width="2"/>
      <path d="M0,272 C140,248 330,262 460,235 C530,220 580,200 616,180 V353 H0 Z" fill="url(#bottom-band)"/>
      <path d="M0,262 C140,238 330,252 460,225 C530,210 580,190 616,170" fill="none" stroke="#7fd0f6" stroke-width="2"/>
    </svg>

    <p class="holder-name">Your Name</p>
    <p class="holder-title">designation</p>

    <p class="contact contact-street">48 Linden Ridge Ct.</p>
    <p class="contact contact-city">Maple Hollow, IL 60999</p>
    <p class="contact contact-phone">Toll Free: 855-555-0142</p>
    <p class="contact contact-email">Email: email@velmira-example.com</p>
    <p class="contact contact-web">Web: www.velmirasolutions-example.com</p>

    <div class="brand-square" aria-hidden="true"></div>
    <div class="brand">
      <p class="brand-name">Velmira</p>
      <p class="brand-sub">Solutions</p>
    </div>
  </section>

  <section class="card card-back" aria-label="Business card back">
    <div class="brand-square" aria-hidden="true"></div>
    <div class="brand">
      <p class="brand-name">Velmira</p>
      <p class="brand-sub">Solutions</p>
    </div>
  </section>

</main>
</body>
</html>
```